Recycling Depot Business Card Design

We need a double sided business card for our recycling depot business. Please include name, position, address, phone, cell, fax, email and website address. Business card should match the colour scheme of our logo and look environmental but modern. I've attached a few business cards from Plume Kettle that I like.

Industry/Entity Type

Recycling

Contact Information for Business Card

Please include name, position, address, phone, cell, fax, email and website address.

Font styles to use
Sans Serif

Requirements
Must have
• Our Logo, Colour Scheme that matches our logo. Use of Colour Gradients and a custom look.

```html
<!DOCTYPE html>
<html lang="en">
<head>
<meta charset="utf-8">
<title>Greenloop Business Card</title>
<link rel="stylesheet" href="https://fonts.googleapis.com/css2?family=Lato:wght@400;700;900&display=swap">
<style>
  :root {
    --page-bg: #e9e6e1;
    --green-deep: #1f7a34;
    --green-mid: #2f9440;
    --green-panel: #5fae3a;
    --green-panel-light: #74bd48;
    --text-light: #eef3e6;
    --text-soft: #d9e8cf;
    --text-dark: #1d4a22;
    --name-green: #8fd14f;
    --mark-fill: #e8efe1;
    --mark-text: #1f7a34;
    --icon-stroke: #9dc98a;
  }
  * { margin: 0; padding: 0; box-sizing: border-box; }
  html, body {
    width: 1200px;
    height: 1047px;
    overflow: hidden;
    background: var(--page-bg);
    font-family: "Lato", sans-serif;
  }
  .card {
    position: absolute;
    left: 151px;
    top: 291px;
    width: 944px;
    height: 513px;
    border-radius: 20px;
    overflow: hidden;
    background: linear-gradient(100deg, var(--green-deep) 0%, var(--green-mid) 55%, #268a3a 72.5%);
    box-shadow: 0 10px 30px rgba(0,0,0,0.12);
  }
  .card__panel {
    position: absolute;
    left: 685px;
    top: 0;
    width: 259px;
    height: 100%;
    background: linear-gradient(180deg, var(--green-panel-light), var(--green-panel));
  }
  .brand {
    position: absolute;
    left: 60px;
    top: 38px;
  }
  .brand__name {
    font-weight: 900;
    font-size: 62px;
    line-height: 1;
    color: var(--text-light);
    letter-spacing: -0.5px;
  }
  .brand__tagline {
    margin-top: 0;
    font-size: 27px;
    line-height: 1.1;
    font-weight: 400;
    color: var(--text-dark);
    letter-spacing: 0.3px;
  }
  .person {
    position: absolute;
    left: 60px;
    top: 196px;
  }
  .person__name {
    font-size: 33px;
    line-height: 1.2;
    font-weight: 700;
    color: var(--name-green);
    letter-spacing: 0.5px;
  }
  .person__role {
    margin-top: 6px;
    font-size: 20px;
    line-height: 1.2;
    color: var(--text-soft);
  }
  .address {
    position: absolute;
    left: 60px;
    top: 282px;
    font-size: 21px;
    line-height: 26px;
    color: var(--text-soft);
  }
  .contacts {
    position: absolute;
    left: 60px;
    top: 345px;
    list-style: none;
  }
  .contacts li {
    display: flex;
    align-items: center;
    height: 28px;
    font-size: 20px;
    color: var(--text-soft);
  }
  .contacts svg {
    width: 18px;
    height: 18px;
    margin-right: 17px;
    fill: none;
    stroke: var(--icon-stroke);
    stroke-width: 1.8;
  }
  .contacts .web-domain { color: var(--name-green); }
  .mark {
    position: absolute;
    left: 489px;
    top: 63px;
    width: 388px;
    height: 388px;
    border-radius: 50%;
    background: var(--mark-fill);
    display: flex;
    align-items: center;
    justify-content: center;
  }
  .mark__name {
    font-size: 54px;
    font-weight: 900;
    color: var(--mark-text);
  }
</style>
</head>
<body>
  <div class="card">
    <div class="card__panel"></div>

    <div class="brand">
      <div class="brand__name">Greenloop</div>
      <div class="brand__tagline">Resource&nbsp;&nbsp;&nbsp;Recovery</div>
    </div>

    <div class="person">
      <div class="person__name">MARA QUILL</div>
      <div class="person__role">Founder &amp; CEO</div>
    </div>

    <div class="address">
      <div>42 Willow Bend Road North</div>
      <div>Unit 7, Fernbrook Park</div>
    </div>

    <ul class="contacts">
      <li>
        <svg viewBox="0 0 18 18"><path d="M3 7c0-3 12-3 12 0v2h-3V7H6v2H3z"/><rect x="4" y="10" width="10" height="5" rx="1"/></svg>
        + 100 5550 2841
      </li>
      <li>
        <svg viewBox="0 0 18 18"><rect x="5" y="2" width="8" height="14" rx="1.5"/><line x1="8" y1="13.5" x2="10" y2="13.5"/></svg>
        + 100 5550 7193
      </li>
      <li>
        <svg viewBox="0 0 18 18"><rect x="5" y="2" width="8" height="4"/><rect x="2" y="6" width="14" height="6" rx="1"/><rect x="5" y="10" width="8" height="6"/></svg>
        + 100 5550 2842
      </li>
      <li>
        <svg viewBox="0 0 18 18"><rect x="2" y="4" width="14" height="10" rx="1"/><path d="M2 4l7 6 7-6"/></svg>
        info@greenloop.com
      </li>
      <li>
        <svg viewBox="0 0 18 18"><circle cx="9" cy="9" r="7"/><path d="M2 9h14M9 2c-3 4-3 10 0 14M9 2c3 4 3 10 0 14"/></svg>
        www.<span class="web-domain">greenloop</span>.com
      </li>
    </ul>

    <div class="mark">
      <span class="mark__name">Greenloop</span>
    </div>
  </div>
</body>
</html>
```